Beauty and cosmetics line, need a new design for my upcoming collection

I need someone to create and new design for my upcoming collection that suits the look and feel of my brand. My brand is woman owned and is called Voranthe Cosmetics based in the UAE. It is a start up business and I am keen to establish myself in the beauty industry. My color palette is very neutral and is consisted of nudes and shades of brown, this upcoming collection will be a big one so I need it to be perfect, to stand out and to be unforgettable. The products are liquid lipsticks, concealer and foundation, the collection name is "Voranthe Essentials"

Target Market(s)

makeup and beauty enthusiasts, makeup artists, general public

Colors

Designer to choose colors to be used in the design.

Requirements
Must have
• authentic identity

```html
<!DOCTYPE html>
<html lang="en">
<head>
<meta charset="utf-8">
<title>Voranthe Essentials – Liquid Lipstick Carton</title>
<link rel="stylesheet" href="https://fonts.googleapis.com/css2?family=Poppins:wght@300;400;500;600&display=swap">
<style>
  :root {
    --paper: #ffffff;
    --panel-top: #fcd6b4;
    --panel-bottom: #e1956a;
    --flap-dark: #e8a579;
    --flap-light: #f9cba6;
    --ink: #b4663e;
    --ink-soft: #a85e3a;
    --cut-line: #3b2a20;
    --foliage: #fff4ea;
  }
  html, body {
    margin: 0;
    padding: 0;
    width: 1111px;
    height: 1200px;
    overflow: hidden;
    background: var(--paper);
  }
  .dieline {
    display: block;
    width: 1111px;
    height: 1200px;
    font-family: "Poppins", sans-serif;
  }
  .cut { stroke: var(--cut-line); stroke-width: 0.9; }
  .panel { fill: url(#panelFill); }
  .tuck-top { fill: url(#tuckTopFill); }
  .tuck-bottom { fill: url(#tuckBottomFill); }
  .dust-flap { fill: url(#dustFill); }
  .body-copy { fill: var(--ink-soft); font-size: 13px; font-weight: 400; }
  .brand-name { fill: var(--ink); font-weight: 600; }
  .brand-line { fill: var(--ink); font-weight: 500; }
  .product-name { fill: var(--ink); font-weight: 400; font-size: 17px; letter-spacing: 1.5px; }
  .web-address { fill: var(--ink); font-weight: 400; font-size: 23px; }
  .spec-line { fill: var(--ink-soft); font-weight: 400; font-size: 14px; }
  .badge { fill: none; stroke: var(--ink-soft); stroke-width: 1.3; }
  .flap-mark { fill: none; stroke: var(--ink); stroke-width: 2; }
  .flap-name { fill: var(--ink); font-weight: 600; font-size: 13px; letter-spacing: 1px; }
  .foliage { fill: url(#foliageGlow); }
</style>
</head>
<body>
<svg class="dieline" viewBox="0 0 1111 1200" xmlns="http://www.w3.org/2000/svg" role="img" aria-label="Voranthe Essentials liquid lipstick carton dieline">
  <defs>
    <linearGradient id="panelFill" gradientUnits="userSpaceOnUse" x1="0" y1="219" x2="0" y2="989">
      <stop offset="0" stop-color="var(--panel-top)"/>
      <stop offset="1" stop-color="var(--panel-bottom)"/>
    </linearGradient>
    <linearGradient id="tuckTopFill" x1="0" y1="0" x2="0" y2="1">
      <stop offset="0" stop-color="var(--flap-dark)"/>
      <stop offset="1" stop-color="var(--flap-light)"/>
    </linearGradient>
    <linearGradient id="tuckBottomFill" x1="0" y1="0" x2="0" y2="1">
      <stop offset="0" stop-color="var(--flap-dark)"/>
      <stop offset="1" stop-color="var(--flap-light)"/>
    </linearGradient>
    <linearGradient id="dustFill" x1="0" y1="0" x2="0" y2="1">
      <stop offset="0" stop-color="var(--flap-light)"/>
      <stop offset="1" stop-color="var(--flap-dark)"/>
    </linearGradient>
    <radialGradient id="foliageGlow">
      <stop offset="0" stop-color="var(--foliage)" stop-opacity="0.35"/>
      <stop offset="1" stop-color="var(--foliage)" stop-opacity="0"/>
    </radialGradient>
  </defs>

  <!-- Top flaps -->
  <polygon class="dust-flap cut" points="317,219 317,195 333,172 426,172 442,195 442,219"/>
  <rect class="tuck-top cut" x="442" y="98" width="126" height="121"/>
  <polygon class="tuck-top cut" points="442,98 462,44 548,44 568,98"/>
  <polygon class="dust-flap cut" points="568,219 568,195 584,172 676,172 692,195 692,219"/>

  <!-- Bottom flaps -->
  <polygon class="tuck-bottom cut" points="317,989 317,1006 336,1039 423,1039 442,1006 442,989"/>
  <rect class="tuck-bottom cut" x="442" y="989" width="126" height="122"/>
  <polygon class="tuck-bottom cut" points="442,1111 462,1156 548,1156 568,1111"/>
  <polygon class="tuck-bottom cut" points="568,989 568,1006 587,1039 673,1039 692,1006 692,989"/>

  <!-- Main panels -->
  <rect class="panel cut" x="317" y="219" width="125" height="770"/>
  <rect class="panel cut" x="442" y="219" width="126" height="770"/>
  <rect class="panel cut" x="568" y="219" width="124" height="770"/>
  <rect class="panel cut" x="692" y="219" width="125" height="770"/>
  <polygon class="panel cut" points="817,219 855,261 855,950 817,989"/>

  <!-- Foliage line art areas -->
  <g role="img" aria-label="Fine white botanical line drawing of leafy stems">
    <ellipse class="foliage" cx="450" cy="290" rx="80" ry="85"/>
    <ellipse class="foliage" cx="520" cy="880" rx="85" ry="120"/>
    <ellipse class="foliage" cx="700" cy="900" rx="80" ry="100"/>
  </g>

  <!-- Top tuck mark -->
  <g class="flap-brand">
    <rect class="flap-mark" x="494" y="128" width="22" height="22"/>
    <text class="flap-name" x="505" y="176" text-anchor="middle">VORANTHE</text>
  </g>

  <!-- Side panel: description -->
  <g class="description">
    <text class="body-copy" transform="translate(353,961) rotate(-90)">Lorem Ipsum is simply dummy text of the printing and typesetting industry. Lorem Ipsum</text>
    <text class="body-copy" transform="translate(371,961) rotate(-90)">has been the industry's standard dummy text ever since the 1500s, when an unknow</text>
    <text class="body-copy" transform="translate(389,961) rotate(-90)">printer took a galley of type and scrambled it to make a type specimen book.</text>
  </g>

  <!-- Front panel: main brand -->
  <g class="front-brand">
    <text class="brand-name" font-size="76" transform="translate(562,986) rotate(-90)">VORANTHE</text>
    <text class="brand-line" font-size="31" letter-spacing="4" transform="translate(562,578) rotate(-90)">ESSENTIALS</text>
  </g>

  <!-- Info panel -->
  <g class="info-panel">
    <circle class="badge" cx="606" cy="266" r="9"/>
    <circle class="badge" cx="630" cy="262" r="8"/>
    <circle class="badge" cx="614" cy="309" r="10"/>
    <rect class="badge" x="600" y="344" width="18" height="18" rx="3"/>
    <text class="spec-line" text-anchor="end" transform="translate(658,250) rotate(-90)">Made in PRC</text>
    <text class="spec-line" text-anchor="end" transform="translate(676,250) rotate(-90)">Net WT. 5.0 gr / 0.18 oz e</text>
    <text class="web-address" transform="translate(636,906) rotate(-90)">www.voranthecosmetics.com</text>
  </g>

  <!-- Back panel -->
  <g class="back-brand">
    <text class="brand-name" font-size="46" transform="translate(778,925) rotate(-90)">VORANTHE</text>
    <text class="brand-line" font-size="21" letter-spacing="3" transform="translate(764,660) rotate(-90)">ESSENTIALS</text>
    <text class="product-name" transform="translate(761,472) rotate(-90)">LIQUID LIPSTICK</text>
  </g>
</svg>
</body>
</html>
```